Business card

Hi Marisa,
can you please design business cards for me?
Based on your Valtrexa design please go crazy (still retain a professional business-solid profile). I would like to use really stylish paper (or different paper types and special prints like partly embossed or partly glossy and contrast the glossiness with matt for instance).
Please keep in mind that I might come back to you in several months if the business requires other print material like stationary, folders, envelopes etc. It all needs to be in line and make a huge impression without going over board and still remain very solid and serious.
I know that's a lot to ask and I apologise but I am really impressed with your work so far and have no doubt that you can spin the wheels again in a great way.
Thanks bunches, Lukas
In order to punch in the right text from the outset, here is some key data:
Valtrexa
Rise beyond today
Lukas Brandow
Chief Executive Level Lifter
+41 76 318 4027
lukas.brandow@valtrexa-example.com
valtrexa-example.com
Industry/Entity Type
Business
Contact Information for Business Card
Valtrexa
Rise beyond today
Lukas Brandow
+41 76 318 4027
valtrexa-example.com

```html
<!DOCTYPE html>
<html lang="en">
<head>
<meta charset="utf-8">
<title>Valtrexa – Business Card Specification</title>
<link rel="stylesheet" href="https://fonts.googleapis.com/css2?family=Fira+Sans:wght@300;400;500;600&display=swap">
<style>
  :root {
    --backdrop-light: #f4f4f5;
    --backdrop-dark: #dcdcde;
    --card-matt: #2b2624;
    --card-matt-deep: #1c1817;
    --card-gloss: #110d0c;
    --ink-white: #ffffff;
    --ink-grey: #8d8784;
    --ink-soft: #b9b4b1;
    --annotation-red: #cf1f2e;
    --spec-ink: #1d1d1f;
  }
  html, body {
    margin: 0;
    padding: 0;
    overflow: hidden;
  }
  body {
    width: 1080px;
    height: 1200px;
    font-family: "Fira Sans", sans-serif;
  }
  .spec-sheet {
    display: block;
    width: 1080px;
    height: 1200px;
  }
  .wordmark {
    font-family: "Fira Sans", sans-serif;
    font-weight: 300;
    font-size: 34px;
    letter-spacing: 5px;
    fill: var(--ink-white);
  }
  .tagline {
    font-weight: 400;
    font-size: 11px;
    letter-spacing: 2.5px;
    fill: var(--ink-grey);
  }
  .holder-name {
    font-weight: 600;
    font-size: 24px;
    letter-spacing: 3px;
    fill: var(--ink-white);
  }
  .holder-role {
    font-weight: 400;
    font-size: 17px;
    fill: var(--ink-grey);
  }
  .contact-line {
    font-weight: 300;
    font-size: 16px;
    fill: var(--ink-grey);
  }
  .contact-web {
    font-weight: 500;
    font-size: 17px;
    fill: var(--ink-white);
  }
  .callout-label {
    font-weight: 400;
    font-size: 21px;
    letter-spacing: 1.5px;
    fill: var(--annotation-red);
  }
  .callout-line {
    stroke: var(--annotation-red);
    stroke-width: 2.5;
    stroke-dasharray: 2 4;
    fill: none;
  }
  .callout-ring {
    stroke: var(--annotation-red);
    stroke-width: 3.5;
    stroke-dasharray: 9 5;
    fill: none;
  }
  .size-title {
    font-weight: 500;
    font-size: 21px;
    letter-spacing: 2px;
    fill: var(--spec-ink);
  }
  .size-values {
    font-weight: 400;
    font-size: 21px;
    letter-spacing: 2px;
    fill: var(--spec-ink);
  }
</style>
</head>
<body>
<svg class="spec-sheet" viewBox="0 0 1080 1200" xmlns="http://www.w3.org/2000/svg">
  <defs>
    <radialGradient id="backdrop-fade" cx="50%" cy="35%" r="75%">
      <stop offset="0" stop-color="var(--backdrop-light)"/>
      <stop offset="1" stop-color="var(--backdrop-dark)"/>
    </radialGradient>
    <linearGradient id="back-finish" x1="0" y1="0" x2="1" y2="1">
      <stop offset="0" stop-color="var(--card-matt)"/>
      <stop offset="1" stop-color="var(--card-matt-deep)"/>
    </linearGradient>
    <clipPath id="front-outline">
      <polygon points="276,199 513,199 513,636 333,881 96,881 96,444"/>
    </clipPath>
  </defs>

  <rect class="backdrop" width="1080" height="1200" fill="url(#backdrop-fade)"/>

  <!-- Front of card: gloss field with matt band -->
  <g class="card card-front" clip-path="url(#front-outline)">
    <rect x="96" y="199" width="417" height="682" fill="var(--card-gloss)"/>
    <polygon class="matt-band" points="96,199 513,199 513,258 96,833" fill="var(--card-matt)"/>
    <text class="wordmark" x="305" y="516" text-anchor="middle">VALTREXA</text>
    <text class="tagline" x="318" y="538" text-anchor="middle">RISE BEYOND TODAY</text>
  </g>

  <!-- Back of card: contact details -->
  <g class="card card-back">
    <polygon points="567,199 803,199 983,444 983,881 747,881 567,636" fill="url(#back-finish)"/>
    <text class="holder-name" x="765" y="455" text-anchor="middle">LUKAS BRANDOW</text>
    <text class="holder-role" x="765" y="483" text-anchor="middle">Chief Executive Level Lifter</text>
    <text class="contact-line" x="765" y="547" text-anchor="middle">+41 76 318 4027</text>
    <text class="contact-line" x="765" y="580" text-anchor="middle">lukas.brandow@valtrexa-example.com</text>
    <text class="contact-web" x="765" y="642" text-anchor="middle">valtrexa-example.com</text>
  </g>

  <!-- Finish callouts -->
  <g class="callout callout-matt-front">
    <text class="callout-label" x="53" y="236">MATT BLACK</text>
    <line class="callout-line" x1="103" y1="247" x2="264" y2="247"/>
    <circle class="callout-ring" cx="281" cy="247" r="17"/>
  </g>
  <g class="callout callout-matt-back">
    <text class="callout-label" x="1033" y="236" text-anchor="end">MATT BLACK</text>
    <line class="callout-line" x1="805" y1="247" x2="969" y2="247"/>
    <circle class="callout-ring" cx="788" cy="247" r="17"/>
  </g>
  <g class="callout callout-gloss">
    <text class="callout-label" x="423" y="816">GLOSS BLACK</text>
    <line class="callout-line" x1="340" y1="828" x2="504" y2="828"/>
    <circle class="callout-ring" cx="323" cy="828" r="17"/>
  </g>
  <g class="callout callout-deboss">
    <circle class="callout-ring" cx="173" cy="512" r="17"/>
    <line class="callout-line" x1="173" y1="529" x2="173" y2="920"/>
    <text class="callout-label" x="137" y="948">“VALTREXA”</text>
    <text class="callout-label" x="137" y="985">IN DEBOSSED</text>
    <text class="callout-label" x="137" y="1022">PRINT</text>
  </g>
  <g class="callout callout-cutting">
    <circle class="callout-ring" cx="700" cy="828" r="17"/>
    <path class="callout-line" d="M708,845 Q728,900 743,957"/>
    <text class="callout-label" x="763" y="951">CNC/LASER</text>
    <text class="callout-label" x="763" y="988">CUTTING</text>
    <text class="callout-label" x="763" y="1025">TO SHAPE</text>
  </g>

  <!-- Card dimensions -->
  <g class="size-spec">
    <text class="size-title" x="540" y="1100" text-anchor="middle">BUSINESS CARD SIZE:</text>
    <text class="size-values" x="540" y="1137" text-anchor="middle">WIDTH: 90 MM  |  HEIGHT: 55 MM</text>
  </g>
</svg>
</body>
</html>
```